LBS Vehicles

We are a general contractor looking to create a vehicle wrap for our vans. I have a logo and general information. We perform the following services:
- New Construction, Additions, and Renovations
- Commercial Build-outs
- Roofing, Siding, Decks, and Exteriors
- Painting and Carpentry

Phone Number is 914-555-0186
email is Office@lbrennickandson.com
website is www.lbrennickandson.com

```html
<!DOCTYPE html>
<html lang="en">
<head>
<meta charset="utf-8">
<title>LBS Vehicles – Van Wrap</title>
<link href="https://fonts.googleapis.com/css2?family=Libre+Baskerville:wght@700&family=Montserrat:wght@600&family=Source+Sans+3:wght@600&display=swap" rel="stylesheet">
<style>
  :root {
    --brand-blue: #0a5aa6;
    --panel-blue: #0b63b5;
    --accent-red: #d3161f;
    --deep-red: #a8141b;
    --wrap-white: #ffffff;
  }
  * { margin: 0; padding: 0; box-sizing: border-box; }
  html, body { width: 1200px; height: 579px; overflow: hidden; background: var(--wrap-white); }
  .wrap {
    position: relative;
    width: 1200px;
    height: 579px;
    background: var(--wrap-white);
    overflow: hidden;
  }
  .side-graphics { position: absolute; inset: 0; }
  .services {
    position: absolute;
    left: 110px;
    top: 141px;
    width: 250px;
    list-style: none;
    font-family: "Source Sans 3", sans-serif;
    font-weight: 600;
    font-size: 18px;
    line-height: 22.5px;
    color: var(--wrap-white);
  }
  .services li { position: relative; padding-left: 10px; margin-bottom: 6px; }
  .services li::before {
    content: "";
    position: absolute;
    left: 0; top: 10px;
    width: 4px; height: 4px;
    border-radius: 50%;
    background: var(--accent-red);
  }
  .services li.spaced { margin-top: 11px; }
  .brand-mark {
    position: absolute;
    left: 382px;
    top: 122px;
    width: 400px;
    text-align: center;
    font-family: "Source Sans 3", sans-serif;
    font-weight: 600;
    font-size: 190px;
    line-height: 180px;
    color: var(--brand-blue);
  }
  .company-name {
    position: absolute;
    left: 346px;
    top: 308px;
    font-family: "Libre Baskerville", serif;
    font-weight: 700;
    font-size: 50px;
    line-height: 1;
    color: var(--brand-blue);
    white-space: nowrap;
  }
  .tagline {
    position: absolute;
    left: 347px;
    top: 368px;
    font-family: "Montserrat", sans-serif;
    font-weight: 600;
    font-size: 15.4px;
    color: var(--deep-red);
    white-space: nowrap;
  }
  .contact {
    position: absolute;
    left: 802px;
    top: 266px;
    list-style: none;
    font-family: "Source Sans 3", sans-serif;
    font-weight: 600;
    font-size: 18px;
    color: var(--brand-blue);
  }
  .contact li { display: flex; align-items: center; gap: 5px; height: 27px; }
  .contact svg { width: 21px; height: 21px; flex: none; }
</style>
</head>
<body>
<main class="wrap">
  <svg class="side-graphics" viewBox="0 0 1200 579" aria-hidden="true">
    <polygon points="0,105 408,105 305,345 290,430 0,430" fill="var(--panel-blue)"/>
    <polygon points="414,105 428,105 320,345 306,345" fill="var(--accent-red)"/>
  </svg>

  <ul class="services">
    <li>New Construction, Additions and Renovations</li>
    <li>Roofing, Siding, Decks, and Exteriors</li>
    <li>Painting and Carpentry</li>
    <li class="spaced">Commercial Build-outs</li>
  </ul>

  <div class="brand-mark">LBS</div>

  <div class="company-name">L. Brennick &amp; Son</div>
  <div class="tagline">RESIDENTIAL &amp; COMMERCIAL GENERAL CONTRACTORS</div>

  <ul class="contact">
    <li>
      <svg viewBox="0 0 22 22" aria-hidden="true">
        <circle cx="11" cy="11" r="9.5" fill="none" stroke="var(--accent-red)" stroke-width="1.6"/>
        <rect x="6" y="7.5" width="10" height="7" fill="none" stroke="var(--accent-red)" stroke-width="1.3"/>
        <polyline points="6,7.5 11,11.5 16,7.5" fill="none" stroke="var(--accent-red)" stroke-width="1.3"/>
      </svg>
      Office@lbrennickandson.com
    </li>
    <li>
      <svg viewBox="0 0 22 22" aria-hidden="true">
        <circle cx="11" cy="11" r="9.5" fill="none" stroke="var(--accent-red)" stroke-width="1.6"/>
        <path d="M7.5 6.5c-.8.6-1 1.8-.4 3.2 1 2.3 2.8 4.2 5.1 5.3 1.4.6 2.6.4 3.2-.4l-1.7-1.8-1.4.7c-1.2-.6-2.2-1.6-2.8-2.8l.7-1.4z" fill="var(--accent-red)"/>
      </svg>
      914-555-0186
    </li>
  </ul>
</main>
</body>
</html>
```